Corporate Business Card

Very professional, Modern, Not to busy, include phone address email, website
(253) 555-0174, 61807 19th Street N, Kent, WA 98517, marcus@kestrelbayholding.com, brelvanindustries.com

Target Market(s)

Manufacturing

Industry/Entity Type

Aero, machining, manufacturing, Off road racing

Contact Information for Business Card

Phone, address email, website

```html
<!DOCTYPE html>
<html lang="en">
<head>
<meta charset="utf-8">
<title>Brelvan Industries – Business Card</title>
<link rel="stylesheet" href="https://fonts.googleapis.com/css2?family=Lato:wght@400;700&display=swap">
<style>
  :root {
    --navy: #16306b;
    --red: #d9232a;
    --muted: #5a6c97;
    --paper: #ffffff;
    --backdrop: #e6e6e6;
  }
  * { margin: 0; padding: 0; box-sizing: border-box; }
  html, body {
    width: 1200px;
    height: 801px;
    overflow: hidden;
    background: var(--backdrop);
    font-family: "Lato", Arial, sans-serif;
  }
  .canvas { position: relative; width: 1200px; height: 801px; }

  .card {
    position: absolute;
    left: 352px;
    width: 521px;
    height: 299px;
    background: var(--paper);
    overflow: hidden;
  }
  .card--front { top: 45px; }
  .card--back { top: 424px; }

  .wordmark {
    position: absolute;
    display: flex;
    align-items: center;
    gap: 8px;
    color: var(--navy);
    font-weight: 700;
    white-space: nowrap;
  }
  .wordmark__square {
    width: 12px;
    height: 12px;
    background: var(--red);
  }
  .card--front .wordmark { top: 34px; right: 30px; font-size: 24px; }
  .card--back .wordmark {
    top: 50%;
    left: 50%;
    transform: translate(-50%, -50%);
    font-size: 30px;
  }

  .holder { position: absolute; left: 0; top: 134px; }
  .holder__bar {
    position: absolute;
    left: 0;
    top: 0;
    width: 12px;
    height: 34px;
    background: var(--red);
  }
  .holder__name {
    margin-left: 17px;
    font-size: 19px;
    font-weight: 700;
    color: var(--navy);
    line-height: 1.1;
    padding-top: 2px;
  }
  .holder__title {
    margin-left: 17px;
    font-size: 13px;
    color: var(--muted);
    margin-top: 2px;
  }

  .contact {
    position: absolute;
    left: 278px;
    list-style: none;
  }
  .contact__item {
    display: flex;
    align-items: center;
    gap: 6px;
    font-size: 13.5px;
    font-weight: 700;
    color: var(--navy);
    height: 22px;
  }
  .contact__item svg { width: 12px; height: 12px; flex: none; fill: var(--red); }
  .contact--address { top: 180px; }
  .contact--lines { top: 218px; }

  .corner {
    position: absolute;
    right: 0;
    bottom: 0;
    width: 0;
    height: 0;
    border-style: solid;
    border-width: 0 0 23px 23px;
    border-color: transparent transparent var(--red) transparent;
  }
</style>
</head>
<body>
<main class="canvas">
  <section class="card card--front" aria-label="Card front">
    <div class="wordmark"><span class="wordmark__square"></span>Brelvan Industries</div>

    <div class="holder">
      <span class="holder__bar"></span>
      <p class="holder__name">DANIEL REYES</p>
      <p class="holder__title">founder &amp; CEO</p>
    </div>

    <ul class="contact contact--address">
      <li class="contact__item">
        <svg viewBox="0 0 12 12" aria-hidden="true"><path d="M6 0a4.3 4.3 0 0 0-4.3 4.3C1.7 7.5 6 12 6 12s4.3-4.5 4.3-7.7A4.3 4.3 0 0 0 6 0zm0 6a1.7 1.7 0 1 1 0-3.4A1.7 1.7 0 0 1 6 6z"/></svg>
        19th Street N, Kent, WA 98517
      </li>
    </ul>

    <ul class="contact contact--lines">
      <li class="contact__item">
        <svg viewBox="0 0 12 12" aria-hidden="true"><path d="M6 0a6 6 0 1 0 0 12A6 6 0 0 0 6 0zm4.6 5.3H8.5a9 9 0 0 0-.8-3.6 4.7 4.7 0 0 1 2.9 3.6zM6 1.3c.6.8 1.1 2.2 1.2 4H4.8c.1-1.8.6-3.2 1.2-4zM4.3 1.7a9 9 0 0 0-.8 3.6H1.4a4.7 4.7 0 0 1 2.9-3.6zM1.4 6.7h2.1c.1 1.4.4 2.6.8 3.6a4.7 4.7 0 0 1-2.9-3.6zM6 10.7c-.6-.8-1.1-2.2-1.2-4h2.4c-.1 1.8-.6 3.2-1.2 4zm1.7-.4c.4-1 .7-2.2.8-3.6h2.1a4.7 4.7 0 0 1-2.9 3.6z"/></svg>
        brelvanindustries.com
      </li>
      <li class="contact__item">
        <svg viewBox="0 0 12 12" aria-hidden="true"><path d="M2.4 0.6l1.9-.3 1.1 2.8-1.4 1a7 7 0 0 0 3.9 3.9l1-1.4 2.8 1.1-.3 1.9c-.1.8-.8 1.3-1.6 1.2C4.9 10.4 1.6 7.1 1.2 2.2 1.1 1.4 1.6.7 2.4.6z"/></svg>
        (253) 555-0174, 61807
      </li>
      <li class="contact__item">
        <svg viewBox="0 0 12 12" aria-hidden="true"><path d="M0 2h12v1.2L6 6.8 0 3.2zM0 4.6l6 3.6 6-3.6V10H0z"/></svg>
        marcus@kestrelbayholding.com
      </li>
    </ul>
  </section>

  <section class="card card--back" aria-label="Card back">
    <div class="wordmark"><span class="wordmark__square"></span>Brelvan Industries</div>
    <span class="corner"></span>
  </section>
</main>
</body>
</html>
```